依頼概要
■依頼の目的/概要
・電子書籍(自己啓発系)の表紙デザインをお願いします。
・電子書籍は、ソルベリアで販売します。pagoraです。

■本の内容
・初出版本です。
・行き詰った人生を何とかしたいなら、人間関係の苦しみを解消したいなら…。自分の『あり方』を変えることによって、人生がうまくいく方向に動きだすよ ということをお伝えする内容になっています。
・作者の経験が、本の元になっています。
・働く世代や、実際に苦しんでいる当事者、ひきこもりの子どもを持つ親など、幅広く読んでもらいたいです。

■デザイン要望
・明るい未来を感じられるような表紙デザインにしてください。
(底抜けに明るいのは×だけど、悲壮感が見えるのも×)
・人物や、絵が入っている表紙が望ましいです。
(イラスト・写真〇。文字のみのデザインは、×)

■本のタイトル
・本のタイトルは、

毎日が「疲れた…」と感じる君へ、ひとつずつ笑顔が戻ってくる、小さな灯火の地図

です。

・サブキャッチに

~胸のざわめきの理由は〝本音の迷子〟だった~

を入れてください。

■ごあいさつ
・その他、ご不明な点がありましたらお気軽にご質問ください。よろしくお願いします。

■ 選んだ理由

Talkvineをつかって、皆さんからいただいた仮案をアンケートさせていただいたところ、
もっとも「いい」「好き」という評価をいただけたのが、今回選ばせていただいたデザインでした。

なぜよかったのか? と聞いてみたところ
「右下のキャラクターが可愛い」
「見ていると、癒される」
「澄ちゃん(私のこと)らしい」
という意見が、出そろいました。

正直に申しますと、私自身も意外だったのですが
多くの人から「このデザインがいちばん私らしい」と言っていただけるので、気になりはじめ、
今では私自身も気に入っております。

■ 提案者全員のお礼・コメント

本当にありがとうございました。

たった一つのデザインを決めるために、たくさんの方から頂いたデザインを落とさなければならないため、胸を痛めました。
落とすには、あまりにも私好みのデザインがあり過ぎました。

中には私の、初出版の、あまり上手とはいえない文章を丁寧に読んでくれる方もいらっしゃり、とても嬉しかったです。
ありがとうございます。
感謝しています。

また何かの折、お世話になることがあれば、よろしくお願いいたします。

```html
<!DOCTYPE html>
<html lang="ja">
<head>
<meta charset="utf-8">
<title>小さな灯火の地図</title>
<link rel="stylesheet" href="https://fonts.googleapis.com/css2?family=Noto+Sans+JP:wght@700;900&family=Noto+Serif+JP:wght@600;700&display=swap">
<style>
  :root {
    --paper: #ffffff;
    --ink: #141414;
    --accent: #e4007f;
    --sub-ink: #2a2a2a;
    --sky-haze: #d9c9d2;
    --sky-top: #6a4e72;
    --sky-mid: #c47a5a;
    --glow: #f2a94e;
    --sea: #3a2a30;
    --sea-deep: #16111a;
  }
  html, body {
    margin: 0;
    padding: 0;
    overflow: hidden;
    background: var(--paper);
  }
  .cover {
    position: relative;
    width: 750px;
    height: 1200px;
    overflow: hidden;
    background: var(--paper);
    font-family: "Noto Sans JP", sans-serif;
  }
  .scene {
    position: absolute;
    left: 0;
    top: 380px;
    width: 750px;
    height: 820px;
  }
  .title {
    position: absolute;
    left: 0;
    top: 0;
    width: 750px;
    margin: 0;
    font-weight: 900;
    color: var(--ink);
  }
  .title span { display: block; position: absolute; white-space: nowrap; }
  .title-stack {
    left: 14px;
    top: 30px;
    font-size: 50px;
    line-height: 1.1;
    letter-spacing: 2px;
  }
  .title-quote {
    left: 108px;
    top: 0;
    font-size: 110px;
    line-height: 1.2;
    letter-spacing: -6px;
  }
  .title-lead {
    left: 14px;
    top: 150px;
    font-size: 78px;
    line-height: 1.2;
    letter-spacing: -1px;
  }
  .title-promise {
    left: 20px;
    top: 246px;
    font-size: 50px;
    line-height: 1.2;
    color: var(--accent);
    letter-spacing: -1px;
  }
  .title-main {
    left: 40px;
    top: 300px;
    font-size: 84px;
    line-height: 1.2;
    color: var(--accent);
  }
  .subtitle {
    position: absolute;
    left: 0;
    top: 402px;
    width: 750px;
    margin: 0;
    text-align: center;
    font-family: "Noto Serif JP", serif;
    font-weight: 700;
    font-size: 31px;
    color: var(--sub-ink);
    text-shadow: 0 0 6px var(--paper), 0 0 3px var(--paper);
  }
  .author {
    position: absolute;
    left: 28px;
    bottom: 22px;
    margin: 0;
    font-family: "Noto Serif JP", serif;
    font-weight: 600;
    font-size: 46px;
    color: var(--paper);
    letter-spacing: 2px;
  }
  .author-roman {
    position: absolute;
    left: 12px;
    top: 820px;
    margin: 0;
    font-family: "Noto Serif JP", serif;
    font-size: 18px;
    line-height: 1;
    color: var(--paper);
    writing-mode: vertical-rl;
    transform: rotate(180deg);
    white-space: nowrap;
  }
</style>
</head>
<body>
<main class="cover">
  <svg class="scene" role="img" aria-label="夕日の海辺で二人の人物が空へ向かって跳び上がる明るい写真" viewBox="0 0 750 820" preserveAspectRatio="none" xmlns="http://www.w3.org/2000/svg">
    <defs>
      <linearGradient id="sky" x1="0.2" y1="0" x2="0.5" y2="1">
        <stop offset="0" stop-color="#ffffff"/>
        <stop offset="0.1" stop-color="var(--sky-haze)"/>
        <stop offset="0.3" stop-color="var(--sky-top)"/>
        <stop offset="0.55" stop-color="var(--sky-mid)"/>
        <stop offset="0.72" stop-color="var(--glow)"/>
        <stop offset="0.86" stop-color="var(--sea)"/>
        <stop offset="1" stop-color="var(--sea-deep)"/>
      </linearGradient>
    </defs>
    <rect width="750" height="820" fill="url(#sky)"/>
  </svg>

  <h1 class="title">
    <span class="title-stack">毎日<br>が</span>
    <span class="title-quote">「疲れた…」</span>
    <span class="title-lead">と感じる君へ、</span>
    <span class="title-promise">ひとつずつ笑顔が戻ってくる、</span>
    <span class="title-main">小さな灯火の地図</span>
  </h1>
  <p class="subtitle">~胸のざわめきの理由は〝本音の迷子〟だった~</p>

  <p class="author-roman">Akikawa Sumiko</p>
  <p class="author">秋川澄子 著</p>
</main>
</body>
</html>
```